Catering Menu Package

I currently have a complete menu package, which we have redesigned as far as content, now I need to it put together in a catalog type format. It is essentially 10-12 pages in length, and will be sent for print production. Upon receiving a final edit
Updates

I have added an example gif to the project.

I did this free hand this basically what I am looking for. please change text and type to whatever you think would look best. This is a total rough design so, feel free to change any and everything. The text for the page is on the word documents. If you need more images let me know I am in the process of getting as many images uploaded for your use.

Reason: I figured we got a late jump with questions, so i am extending a few days .

Target Market(s)

The target market is business who wish to have catered luncheons, breakfasts , meetings

Industry/Entity Type

Catering

Requirements
Must have
• I have attached a copy of the text that what we want in the package, our logo, and i have also attached a catering package of another company to give you an idea what the finished product will be
Should not have
• It should not look identical to the example catering packages, these are for some inspiration we want our own design with the same type of look and feel

```html
<!DOCTYPE html>
<html lang="en">
<head>
<meta charset="utf-8">
<title>Desserts Menu</title>
<link href="https://fonts.googleapis.com/css2?family=Cinzel+Decorative:wght@700&family=Gelasio:ital,wght@0,400;0,700;1,400&display=swap" rel="stylesheet">
<style>
  :root {
    --cream: #f7eda7;
    --cream-light: #fbf4c6;
    --orange: #e6701c;
    --green: #b4c03a;
    --frame: #c6ca4c;
    --grey-text: #a7a69c;
    --price: #b2b1a6;
    --white: #ffffff;
    --ink: #2b2b2b;
  }
  * { margin: 0; padding: 0; box-sizing: border-box; }
  html, body { width: 927px; height: 1200px; overflow: hidden; }
  body { font-family: "Gelasio", Georgia, serif; background: var(--white); }
  .page {
    position: relative; width: 927px; height: 1200px; overflow: hidden;
    background: linear-gradient(180deg, #f9f0b2 0%, var(--cream) 100%);
  }
  .decor-glow {
    position: absolute; left: 540px; top: 220px; width: 400px; height: 660px;
    background: radial-gradient(ellipse at 50% 40%, rgba(255,250,215,0.75) 0%, rgba(255,250,215,0.35) 45%, rgba(255,250,215,0) 72%);
  }
  .footer-band {
    position: absolute; left: 0; top: 901px; width: 927px; height: 299px;
    background: var(--white); border-top: 4px solid var(--orange);
  }
  .title {
    position: absolute; top: 58px; width: 100%; text-align: center;
    font-family: "Cinzel Decorative", "Times New Roman", serif;
    font-weight: 700; font-size: 34px; color: var(--orange); letter-spacing: 2px;
  }
  .item-name {
    position: absolute; left: 30px; font-weight: 700; font-size: 22px; color: var(--green);
    letter-spacing: 0.3px;
  }
  .item-desc {
    position: absolute; left: 30px; font-style: italic; font-size: 17.5px; line-height: 27px;
    color: var(--grey-text); letter-spacing: 1.6px;
  }
  .price {
    position: absolute; right: 26px; font-weight: 700; font-size: 21px; color: var(--price);
  }
  .photo {
    position: absolute; border: 11px solid var(--frame); background-clip: padding-box;
  }
  .photo-fountain { left: 200px; top: 788px; width: 240px; height: 303px;
    background-color: #6b3a22;
    background-image: linear-gradient(160deg, #8a5a3a 0%, #4a2616 55%, #c9a640 100%); }
  .photo-cakepops { left: 391px; top: 901px; width: 360px; height: 282px;
    background-image: linear-gradient(135deg, #e8a6bf 0%, #d0607e 50%, #f2d2dc 100%); }
  .photo-petitfours { left: 715px; top: 786px; width: 212px; height: 294px;
    background-image: linear-gradient(150deg, #f4eeee 0%, #b53a42 45%, #5a1e1a 100%); }
  .brand-box {
    position: absolute; left: 0; top: 920px; width: 186px; height: 270px;
    border: 11px solid var(--frame); background: var(--white);
    display: flex; flex-direction: column; align-items: center; justify-content: center; gap: 18px;
  }
  .brand-mark { width: 70px; height: 70px; border-radius: 50%; background: var(--orange); }
  .brand-name {
    font-weight: 700; font-size: 22px; line-height: 26px; color: var(--ink);
    text-align: center; text-transform: lowercase;
  }
</style>
</head>
<body>
<main class="page">
  <div class="decor-glow" role="img" aria-label="Soft pale flower silhouettes decorating the background"></div>

  <h1 class="title">Desserts</h1>

  <h2 class="item-name" style="top:133px">Homemade Cookies, Brownies &amp; Blondies</h2>
  <span class="price" style="top:135px">$X.XX per person</span>

  <h2 class="item-name" style="top:181px">Dessert Miniatures</h2>
  <p class="item-desc" style="top:213px">Homemade Cookies, Brownies, Blondies, Petit Fours,<br>Miniature Chocolate Mousse Cups &amp; Crème Puffs</p>
  <span class="price" style="top:236px">$X.XX per person</span>
  <p class="item-desc" style="top:277px">Strawberry Shortcake &amp; Chocolate Brownie Mousse<br>Parfaits</p>
  <span class="price" style="top:276px">$X.XX per person</span>

  <h2 class="item-name" style="top:348px">New York Style Cheesecake Bar</h2>
  <p class="item-desc" style="top:380px">With warm chocolate sauce, caramel, strawberries<br>Cherries &amp; whipped topping</p>
  <span class="price" style="top:406px">$X.XX per person</span>

  <h2 class="item-name" style="top:453px">Ice Cream Sundae Bar</h2>
  <p class="item-desc" style="top:484px">Hand Dipped Ice Cream Cups.Served With Toppings:<br>Chopped Nuts, Chocolate Chips, Crushed Sandwich<br>Cookies,Rainbow Sprinkles, Cherries, Whipped<br>Topping,Chocolate Syrup, Caramel, Pineapple,<br>Strawberry</p>

  <h2 class="item-name" style="top:640px">Chocolate Fountain</h2>
  <p class="item-desc" style="top:674px">Milk Chocolate, Dark Chocolate Or White Chocolate.<br>Marshmallows, Fresh Strawberries, Bananas, Pineapple,<br>Cookies, Rice Crispy Treats, Pretzels, Angle Cake, Pound<br>Cake</p>

  <div class="footer-band"></div>

  <div class="photo photo-fountain" role="img" aria-label="Photo of a chocolate fountain with pineapple and bananas"></div>
  <div class="photo photo-cakepops" role="img" aria-label="Photo of pink cake pops on sticks"></div>
  <div class="photo photo-petitfours" role="img" aria-label="Photo of chocolate petit fours on a white plate"></div>

  <div class="brand-box">
    <div class="brand-mark"></div>
    <div class="brand-name">harbor<br>field<br>caterers</div>
  </div>
</main>
</body>
</html>
```